Marketing Brochure For Tallbrook LLC for marketing and advertising purposes.A slick and modern design. I have added in the attachment a PDF called Tallbrook Profile which is the old version of this new one we are creating but can give you an idea of what I am looking for. I also have a Word document called New Consulting Document that lists each topic, where the attached images go, and the wording that goes in each. The total brochure should be between 8 and 12 pages.

Industry/Entity Type

Credit Card

Font styles to use
Serif

Colors
f78f20
886aae

Requirements
Must have
• A slick and modern design. I have added in the attachment a PDF called Tallbrook Profile which is the old version of this new one we are creating but can give you an idea of what I am looking for. I also have a Word document called New Consulting Document that lists each topic, where the attached images go, and the wording that goes in each. The total brochure should be between 8 and 12 pages.

```html
<!DOCTYPE html>
<html lang="en">
<head>
<meta charset="utf-8">
<title>Tallbrook LLC Brochure – Consulting &amp; Services</title>
<link rel="stylesheet" href="https://fonts.googleapis.com/css2?family=Montserrat:wght@600;700;800;900&family=Open+Sans:wght@400;600&display=swap">
<style>
  :root {
    --orange: #f78f20;
    --pink: #e8566f;
    --purple: #886aae;
    --violet: #7a59a8;
    --ink: #2b2b2b;
    --body: #3d3d3d;
    --paper: #f7f7f7;
    --backdrop: #d9d9d9;
  }
  * { box-sizing: border-box; margin: 0; padding: 0; }
  html, body { width: 1200px; height: 833px; overflow: hidden; background: var(--backdrop); }
  body { font-family: "Open Sans", Arial, sans-serif; color: var(--body); }

  .spread {
    position: absolute; left: 45px; top: 24px; width: 1110px; height: 785px;
    display: flex; box-shadow: 0 10px 30px rgba(0,0,0,.18);
  }
  .page { position: relative; width: 555px; height: 785px; background: var(--paper); overflow: hidden; }
  .page--left { background: linear-gradient(90deg, #fafafa 85%, #ececec); }
  .page--right { background: linear-gradient(90deg, #ececec, #fafafa 15%); }

  .page-title { position: absolute; font-family: "Montserrat", Arial, sans-serif; font-weight: 900; font-size: 30px; letter-spacing: 1px; color: #141414; }
  .title-block { position: absolute; width: 92px; height: 58px; background: linear-gradient(90deg, var(--orange), var(--pink)); }

  p { font-size: 8.6px; line-height: 1.42; text-align: justify; }
  .section-heading { font-family: "Montserrat", Arial, sans-serif; font-weight: 700; font-size: 15px; color: var(--violet); position: absolute; }

  .placeholder { position: absolute; border-radius: 2px; }

  .footer-band {
    position: absolute; height: 30px; display: flex; align-items: center; gap: 10px;
    padding: 0 18px; color: #fff; font-size: 11px; font-weight: 600;
    background: linear-gradient(90deg, var(--violet), var(--pink));
  }
  .footer-line { position: absolute; height: 1px; background: linear-gradient(90deg, var(--pink), var(--orange)); }

  .values-diagram { position: absolute; }
  .values-diagram text { font-family: "Montserrat", Arial, sans-serif; font-weight: 700; font-size: 6.5px; fill: #fff; text-anchor: middle; }
  .values-diagram .brand { fill: var(--violet); font-size: 11px; font-family: "Open Sans", Arial, sans-serif; font-weight: 600; }
</style>
</head>
<body>
<main class="spread">

  <!-- Left page -->
  <section class="page page--left">
    <div class="title-block" style="left:52px;top:30px;"></div>
    <h1 class="page-title" style="left:60px;top:48px;">CONSULTING</h1>

    <p style="position:absolute;left:60px;top:110px;width:435px;">
      Tallbrook LLC provides consulting services and specializes in the credit and collection industry. The area of focus for consulting is debt collection agencies, creditors, asset buyers, and solution providers. Our consulting services are focused on two avenues; staying ahead of the curve and turning challenging situations into positive experiences. Tallbrook offers a holistic approach to its consulting but also offers an ala carte process by focusing in the areas of Operational Excellence, Compliance, Employee Development, Business Development, Client Experience, Information Technology, and Public Relations. Tallbrook takes great pride in getting organizations to obtain maximum output with minimum input while increasing efficiency, effectiveness, and profitability.
    </p>

    <div class="placeholder" role="img" aria-label="Consulting illustration with icons for goal, expert, knowledge, strategy, advice, support and success"
         style="left:60px;top:215px;width:435px;height:130px;background:linear-gradient(135deg,#e9e6ef,#f3ece4);"></div>

    <p style="position:absolute;left:60px;top:370px;width:215px;">
      Tallbrook also specializes in leadership coaching with a focus on mid-level, senior, and executive level management. We have found over the years that most organizations do a good enough job in training their front line employees but fail to train the leaders that are leading the organization. That is where Tallbrook comes in, with over two decades of training all levels of employees our training program is customized to reach upper level management. We focus on where the individual or the organization wants or needs to be in order to be the most productive individually and corporately. Our program interacts with everyone on their level in a way that energizes them to achieve extraordinary results with desired objectives and goals in mind. It is important for us to identify and understand each situation and priorities of the individual and organization so that each unique situation is strategized on how to reach them while providing a learning environment that teaches them to overcome obstacles that rise along the journey. Tallbrook Leadership focus on five avenues; Mindset, Purpose, Caring, Communication, and Courage.
    </p>

    <svg class="values-diagram" style="left:290px;top:395px;" width="210" height="190" viewBox="0 0 210 190" aria-label="Five leadership avenues">
      <circle cx="105" cy="90" r="70" fill="none" stroke="#333" stroke-width="1.2" stroke-dasharray="3 3"/>
      <circle cx="105" cy="90" r="33" fill="#fff" stroke="#333" stroke-width="1.5"/>
      <text class="brand" x="105" y="94">Tallbrook</text>
      <circle cx="140" cy="30" r="18" fill="#2f6f9a" stroke="#fff" stroke-width="2"/><text x="140" y="32">MINDSET</text>
      <circle cx="178" cy="102" r="18" fill="#c4436b" stroke="#fff" stroke-width="2"/><text x="178" y="104">PURPOSE</text>
      <circle cx="132" cy="162" r="18" fill="#ec6a6f" stroke="#fff" stroke-width="2"/><text x="132" y="164">CARING</text>
      <circle cx="46" cy="130" r="18" fill="#3b8fb0" stroke="#fff" stroke-width="2"/><text x="46" y="128">COMMU-</text><text x="46" y="136">NICATION</text>
      <circle cx="42" cy="55" r="18" fill="#4aa7c9" stroke="#fff" stroke-width="2"/><text x="42" y="57">COURAGE</text>
    </svg>

    <div class="placeholder" role="img" aria-label="Leadership coaching lettering graphic"
         style="left:330px;top:600px;width:150px;height:46px;background:linear-gradient(90deg,#dfe6ef,#e8f0dc);"></div>

    <div class="footer-band" style="left:0;top:680px;width:270px;">
      <svg width="11" height="11" viewBox="0 0 12 12" aria-hidden="true"><circle cx="6" cy="6" r="5" fill="none" stroke="#fff"/><path d="M1 6h10M6 1c3 3 3 7 0 10M6 1c-3 3-3 7 0 10" fill="none" stroke="#fff" stroke-width=".8"/></svg>
      <span>www.tallbrookllc.com</span>
    </div>
    <div class="footer-line" style="left:270px;top:695px;width:285px;"></div>
  </section>

  <!-- Right page -->
  <section class="page page--right">
    <div class="title-block" style="left:40px;top:36px;"></div>
    <h1 class="page-title" style="left:48px;top:58px;">SERVICES PROVIDED</h1>

    <h2 class="section-heading" style="left:48px;top:118px;">Operational Excellence</h2>
    <p style="position:absolute;left:48px;top:142px;width:460px;">
      We will provide an exhaustive and unbiased review of your organizations current collection strategies from a cradle to grave work flow standpoint. This will include best practices from across the industry and provide you with templated procedures, necessary reporting, workforce management, and ensuring your organization is working with the right technology providers at the right cost to the organization.
    </p>
    <p style="position:absolute;left:48px;top:205px;width:240px;">
      We will provide an exhaustive and unbiased review of your organizations current collection strategies from a cradle to grave work flow standpoint. This will include best practices from across the industry and provide you with templated procedures, necessary reporting, workforce management, and ensuring your organization is working with the right technology providers at the right cost to the organization.
    </p>
    <p style="position:absolute;left:48px;top:290px;width:240px;">
      If warranted, a full and complete review of the organizations profit and loss statement would be reviewed and findings shared with executive management to identify areas and trends where the strengths and areas of opportunities are.
    </p>
    <div class="placeholder" role="img" aria-label="Compliance concept image with surrounding icons"
         style="left:305px;top:215px;width:190px;height:110px;background:linear-gradient(135deg,#efe9ee,#e6e3e7);border:4px solid #f2dbe2;"></div>

    <h2 class="section-heading" style="left:48px;top:352px;">Employee Development</h2>
    <p style="position:absolute;left:48px;top:378px;width:460px;">
      When it comes to any organization, the number one asset is the employees. If you take care of your employees, they will take care of your consumers, and that will take care of your organization. Ultimately, all we do starts and ends with our employees and we have developed a training curriculum from the first day all the way through years of gainful employment.
    </p>
    <p style="position:absolute;left:48px;top:436px;width:460px;">
      Unfortunately, the debt collection industry operates under several strict liability statutes which means all employees must always be perfect. We all realize that is an unreasonable request but a request that must be adhered to nonetheless. We spend a lot of time with employees on how to operate under these statutes and what they can do to mitigate violating the various laws they must follow but still performing at optimal levels.
    </p>
    <p style="position:absolute;left:48px;top:505px;width:240px;">
      We will help build a foundation and create or enhance your current employee development program which includes orientation, initial and ongoing training, employee handbooks, training manuals, and talent evaluations and reviews for each department.
    </p>
    <div class="placeholder" role="img" aria-label="People development chart with train, educate, empower and reward"
         style="left:305px;top:520px;width:190px;height:120px;background:linear-gradient(135deg,#f1e6df,#e9e2e6);border:4px solid #f2dbe2;"></div>

    <div class="footer-line" style="left:0;top:695px;width:270px;"></div>
    <div class="footer-band" style="left:270px;top:680px;width:285px;">
      <svg width="11" height="11" viewBox="0 0 12 12" aria-hidden="true"><circle cx="6" cy="6" r="5" fill="none" stroke="#fff"/><path d="M1 6h10M6 1c3 3 3 7 0 10M6 1c-3 3-3 7 0 10" fill="none" stroke="#fff" stroke-width=".8"/></svg>
      <span>www.tallbrookllc.com</span>
    </div>
  </section>

</main>
</body>
</html>
```